Business Card Design Project

I need some business cards with the logo you did for us (attached)
I am looking for a coulourful yet serious business card

We do market research
on the back I want the logo

on the front my name : Corinne Valdessac
position : Manager
address : Brume Analytica Sarl - 27 Rue des tanneurs
1847 Glarency - Switzerland
corinne.valdessac@brumeanalytica.ch
Tel : +4122 934 07 58
Mob France :+33 671 42 8356
Mob Italy +39 347 520 8163

The tree of the logo could also be used alone

THE BACKGROUND COLOR ON THE FRONT HAS TO BE WHITE, ON THE BACK YU CAN TRY OHER COLOUR BUT HOMOGENEOUS (NOT EXPENSIVE TO PRINT)

Target Market(s)

multinational companies or other market research companies

Industry/Entity Type

Market Research

Requirements
Must have
• logo on the back
and all the info above

```html
<!DOCTYPE html>
<html lang="en">
<head>
<meta charset="utf-8">
<title>Brume Analytica – Stationery</title>
<link rel="stylesheet" href="https://fonts.googleapis.com/css2?family=Arimo:wght@400;700&family=Ubuntu:wght@400&display=swap">
<style>
  :root {
    --stage: #000000;
    --paper: #ffffff;
    --faint: #e9e9ea;
    --brand-pink: #d6245b;
    --name-red: #b0263a;
    --divider: #7b2d2d;
    --ink: #111111;
  }
  * { margin: 0; padding: 0; box-sizing: border-box; }
  html, body { width: 1200px; height: 900px; overflow: hidden; background: var(--stage); }
  .canvas { position: relative; width: 1200px; height: 900px; background: var(--stage); font-family: "Arimo", Arial, sans-serif; }

  .wordmark { font-family: "Ubuntu", sans-serif; font-weight: 400; color: var(--brand-pink); white-space: nowrap; letter-spacing: -0.5px; }
  .mark-dot { position: absolute; border-radius: 50%; background: var(--brand-pink); }
  .faint-disc { position: absolute; border-radius: 50%; background: var(--faint); }

  /* Letterhead */
  .letterhead { position: absolute; left: 80px; top: 124px; width: 460px; height: 648px; background: var(--paper); overflow: hidden; }
  .letterhead .faint-disc { left: 19px; top: 134px; width: 420px; height: 420px; }
  .letterhead .mark-dot { left: 42px; top: 540px; width: 44px; height: 44px; }
  .letterhead .wordmark { position: absolute; left: 14px; top: 592px; font-size: 23px; }
  .letterhead .divider { position: absolute; left: 185px; top: 592px; width: 2px; height: 56px; background: var(--divider); }
  .letterhead .address { position: absolute; left: 202px; top: 597px; font-size: 11px; line-height: 15px; color: var(--ink); }

  /* Business card – front */
  .card { position: absolute; width: 561px; height: 299px; border-radius: 14px; overflow: hidden; }
  .card-front { left: 563px; top: 136px; background: var(--paper); }
  .card-front .faint-disc { left: 170px; top: 4px; width: 220px; height: 220px; }
  .card-front .mark-dot { left: 82px; top: 138px; width: 62px; height: 62px; }
  .card-front .wordmark { position: absolute; left: 36px; top: 212px; font-size: 31px; }
  .contact { position: absolute; left: 315px; top: 40px; color: var(--ink); }
  .contact .person { font-size: 19px; font-weight: 700; color: var(--name-red); line-height: 22px; }
  .contact .role { font-size: 13.5px; color: var(--brand-pink); margin-top: 3px; }
  .contact .lines { font-size: 11.5px; line-height: 17.5px; margin-top: 53px; }
  .contact .postal { font-size: 11.5px; line-height: 17.5px; margin-top: 13px; }

  /* Business card – back */
  .card-back { left: 565px; top: 460px; background: var(--brand-pink); }
  .card-back .mark-dot { left: 246px; top: 62px; width: 70px; height: 70px; background: var(--ink); }
  .card-back .wordmark { position: absolute; left: 0; right: 0; top: 150px; text-align: center; font-size: 40px; color: var(--ink); }
</style>
</head>
<body>
<main class="canvas">

  <section class="letterhead" aria-label="Letterhead">
    <div class="faint-disc" aria-hidden="true"></div>
    <div class="mark-dot" aria-hidden="true"></div>
    <div class="wordmark">brume analytica</div>
    <div class="divider" aria-hidden="true"></div>
    <p class="address">Brume Analytica Sarl -&nbsp; 27 Rue des tanneurs<br>1847 Glarency - Switzerland</p>
  </section>

  <section class="card card-front" aria-label="Business card front">
    <div class="faint-disc" aria-hidden="true"></div>
    <div class="mark-dot" aria-hidden="true"></div>
    <div class="wordmark">brume analytica</div>
    <div class="contact">
      <p class="person">Corinne Valdessac</p>
      <p class="role">Manager</p>
      <p class="lines">
        corinne.valdessac@brumeanalytica.ch<br>
        Tel :&nbsp; +4122 934 07 58<br>
        Mob France :+33 671 42 8356<br>
        Mob Italy&nbsp; +39 347 520 8163
      </p>
      <p class="postal">
        Brume Analytica Sarl -<br>
        27 Rue des tanneurs<br>
        1847 Glarency - Switzerland
      </p>
    </div>
  </section>

  <section class="card card-back" aria-label="Business card back">
    <div class="mark-dot" aria-hidden="true"></div>
    <div class="wordmark">brume analytica</div>
  </section>

</main>
</body>
</html>
```